Existing App Needs A Facelift

The Kelvo Massager is an existing mobile application that needs an update. I built this way before the tavifone 5 or 5s as well as iOs 7 came out so there is obvious room for improvement. You can find the app here https://apps.storevane.test/us/app/kelvo-massager/id804512736?mt=8 and see the creative direction it needs to go. I need a new appcon that reflects the iOs 7 design structure.

You can download the PSD files from here :
https://www.filecrate.test/sh/x7qa2m9pd4tz/ReWnVbtkLu

Colors

Designer to choose colors to be used in the design.

Requirements
Must have
• It must have the hand-held massager.

```html
<!DOCTYPE html>
<html lang="en">
<head>
<meta charset="utf-8">
<title>Kelvo Massager – App Redesign</title>
<link rel="stylesheet" href="https://fonts.googleapis.com/css2?family=Roboto:wght@300;400;500;700&display=swap">
<style>
:root{
  --orange:#f07a33;
  --orange-deep:#e8622a;
  --orange-light:#f69a52;
  --bg:#e6e6e6;
  --panel:#efeff4;
  --white:#ffffff;
  --line:#d6d6da;
  --text:#1a1a1a;
  --muted:#8e8e93;
  --green:#4cd964;
  --pink:#ff2d55;
  --tab-grey:#929292;
}
*{box-sizing:border-box;margin:0;padding:0}
html,body{width:1200px;height:1000px;overflow:hidden}
body{background:linear-gradient(180deg,#ececec 0%,#dedede 100%);font-family:"Roboto",Arial,sans-serif;color:var(--text);position:relative}
.screen{position:absolute;background:var(--panel);overflow:hidden;box-shadow:0 1px 4px rgba(0,0,0,.25)}
.status{height:18px;display:flex;align-items:center;justify-content:space-between;padding:0 7px;font-size:9px;color:#fff;position:relative}
.status .time{position:absolute;left:0;right:0;text-align:center;pointer-events:none}
.battery{display:inline-block;width:18px;height:8px;border:1px solid currentColor;border-radius:2px;margin-left:3px;vertical-align:-1px;position:relative}
.battery::after{content:"";position:absolute;inset:1px;background:currentColor}
.appbar{background:var(--orange)}
.navbar{height:34px;display:flex;align-items:center;justify-content:center;position:relative;color:#fff;font-size:14px;font-weight:500}
.navbar .back{position:absolute;left:8px;font-weight:400;font-size:14px;display:flex;align-items:center;gap:4px;color:#ffd9c2}
.navbar .back svg{width:9px;height:15px}
.navbar .right{position:absolute;right:10px;font-weight:400;color:#fff}
.tabbar{position:absolute;left:0;right:0;bottom:0;height:40px;background:#f7f7f7;border-top:1px solid var(--line);display:flex}
.tab{flex:1;display:flex;flex-direction:column;align-items:center;justify-content:center;gap:2px;font-size:7px;color:var(--tab-grey)}
.tab svg{width:20px;height:20px;fill:none;stroke:currentColor;stroke-width:1.2}
.tab.active{color:var(--orange)}
.art{background:radial-gradient(circle at 50% 35%,var(--orange-light),var(--orange-deep) 70%)}
.massager-art{position:absolute;border-radius:40% 40% 46% 46%}

/* home */
.home{left:53px;top:107px;width:260px;height:458px;background:#fff}
.home .navbar{height:36px}
.home .massager-art{left:44px;top:108px;width:170px;height:175px}
.home .hint{position:absolute;top:318px;width:100%;text-align:center;color:var(--orange);font-size:21px;font-weight:300;line-height:28px}

/* intensity */
.intensity{left:352px;top:28px;width:256px;height:454px}
.row{position:absolute;left:0;right:0;height:36px;background:#fff;border-top:1px solid var(--line);border-bottom:1px solid var(--line);display:flex;align-items:center;padding:0 12px 0 6px;font-size:13px}
.row .wave{width:30px;height:26px;margin-right:8px;stroke:var(--orange);fill:none;stroke-width:1.2}
.row .label{flex:1}
.toggle{width:40px;height:24px;border-radius:12px;border:1.5px solid #e2e2e2;background:#fff;position:relative}
.toggle::after{content:"";position:absolute;top:0;left:0;width:21px;height:21px;border-radius:50%;background:#fff;box-shadow:0 1px 3px rgba(0,0,0,.3)}
.toggle.on{background:var(--green);border-color:var(--green)}
.toggle.on::after{left:16px}

/* timer */
.timer{left:632px;top:28px;width:256px;height:454px}
.picker{position:absolute;top:52px;left:0;right:0;height:145px;background:#fff;font-size:13px;color:#9a9a9a}
.picker .n{position:absolute;text-align:right}
.picker .sel{position:absolute;top:59px;left:0;right:0;height:28px;border-top:1px solid var(--line);border-bottom:1px solid var(--line);font-size:16px;color:var(--text)}
.picker .sel span{position:absolute;top:5px}
.timer .row{top:200px;padding-left:12px}
.circle-btn{position:absolute;top:270px;width:60px;height:60px;border-radius:50%;display:flex;align-items:center;justify-content:center;font-size:13px}
.start{left:47px;border:1.5px solid var(--green);color:var(--green)}
.pause{left:149px;border:1.5px solid #aaa;color:#888}

/* share */
.share{left:915px;top:28px;width:256px;height:454px;background:#bdbdbd}
.share .stage{position:absolute;top:52px;left:0;right:0;height:266px;background:#bcbcbc}
.share .massager-art{left:54px;top:48px;width:160px;height:170px}
.sheet{position:absolute;top:318px;left:0;right:0;height:91px;background:#f5f5f5;display:flex;justify-content:space-around;padding-top:16px}
.share-item{display:flex;flex-direction:column;align-items:center;gap:5px;font-size:8px;color:#222}
.share-item i{display:block;width:48px;height:48px;border-radius:11px}
.cancel{position:absolute;bottom:0;left:0;right:0;height:45px;background:#f5f5f5;border-top:1px solid #ddd;display:flex;align-items:center;justify-content:center;color:var(--orange);font-size:18px}

/* music */
.music{left:492px;top:508px;width:256px;height:457px;background:#fff}
.track{position:absolute;left:0;right:0;height:47px;border-bottom:1px solid #e3e3e3;display:flex;align-items:center;padding-left:12px;gap:8px}
.cover{width:40px;height:40px;flex:none}
.track .meta{overflow:hidden;white-space:nowrap}
.track .title{font-size:13px;font-weight:500}
.track .sub{font-size:9px;color:#333;margin-top:3px}
.track .sub em{font-style:normal;color:var(--muted)}
.player{position:absolute;bottom:40px;left:0;right:0;height:37px;border-top:1px solid var(--line);background:#f7f7f7;display:flex;justify-content:space-around;align-items:center;padding:0 16px}
.player svg{width:22px;height:22px;fill:var(--orange-deep)}

/* albums */
.albums{left:775px;top:508px;width:256px;height:457px;background:#fff}
.albums .status{color:#000}
.albums .battery{color:#000}
.albums .battery::after{background:var(--green)}
.albums .navbar{color:#000;border-bottom:1px solid #ddd;background:#f8f8f8}
.albums .navbar .back{color:var(--pink);left:6px}
.albums .now{position:absolute;right:6px;top:8px;font-size:8px;color:var(--pink);text-align:right;line-height:9px;font-weight:400;padding-right:12px}
.albums .now::after{content:"";position:absolute;right:0;top:5px;width:7px;height:7px;border-right:2px solid var(--pink);border-bottom:2px solid var(--pink);transform:rotate(-45deg)}
.section{position:absolute;left:0;right:0;height:14px;background:#f2f2f2;font-size:11px;font-weight:500;padding-left:12px;color:#555;line-height:14px;z-index:2}
.album{position:absolute;left:12px;right:24px;height:80px;border-bottom:1px solid #e3e3e3;display:flex;align-items:center;gap:9px;overflow:hidden}
.album .cover{width:70px;height:70px}
.album .meta{white-space:nowrap;overflow:hidden}
.album .name{font-size:13px;font-weight:500}
.album .artist{font-size:12px}
.album .count{font-size:8px;margin-top:3px}
.album.clipped{align-items:flex-start}
.album.clipped .cover{height:32px}
.index{position:absolute;right:4px;top:86px;width:10px;display:flex;flex-direction:column;align-items:center;font-size:7px;line-height:10.4px;color:var(--pink)}
.albums .tabbar{background:#f8f8f8;z-index:3}
.albums .tab.active{color:var(--pink)}

/* app icon */
.appicon{position:absolute;left:85px;top:725px;width:205px;height:205px;border-radius:46px;background:#fff;box-shadow:0 1px 3px rgba(0,0,0,.08)}
.appicon .massager-art{left:28px;top:12px;width:150px;height:182px}
</style>
</head>
<body>

<!-- Home screen -->
<section class="screen home">
  <div class="appbar">
    <div class="status"><span>●●●●○ Carrier</span><span class="time">4:34 PM</span><span>100% <i class="battery"></i></span></div>
    <div class="navbar">Kelvo Massager</div>
  </div>
  <div class="massager-art art" role="img" aria-label="Hand-held massager illustration in orange and grey"></div>
  <p class="hint">Tap to start<br>Double tap to stop</p>
  <nav class="tabbar">
    <div class="tab active"><svg viewBox="0 0 20 20"><path d="M3 10L10 3l7 7M5 8v9h4v-5h2v5h4V8" fill="currentColor" stroke="none" opacity=".9"/></svg>Home</div>
    <div class="tab"><svg viewBox="0 0 20 20"><path d="M6 18c-2-2-3-5-3-7l2-1 2 3V4a1 1 0 012 0v6V2.5a1 1 0 012 0V10V3.5a1 1 0 012 0V11V6a1 1 0 012 0v7c0 3-2 5-4 5z"/></svg>Intensity</div>
    <div class="tab"><svg viewBox="0 0 20 20"><circle cx="10" cy="11" r="7.5"/><path d="M10 11L7 7M10 3.5V2"/></svg>Timer</div>
    <div class="tab"><svg viewBox="0 0 20 20"><path d="M7 16V4l10-2v12"/><circle cx="5" cy="16" r="2"/><circle cx="15" cy="14" r="2"/></svg>Music</div>
    <div class="tab"><svg viewBox="0 0 20 20"><path d="M7 7H4v11h12V7h-3M10 13V2M7 5l3-3 3 3"/></svg>Share</div>
  </nav>
</section>

<!-- Intensity screen -->
<section class="screen intensity">
  <div class="appbar">
    <div class="status"><span>●●●●○ Carrier</span><span class="time">4:34 PM</span><span>100% <i class="battery"></i></span></div>
    <div class="navbar"><span class="back"><svg viewBox="0 0 9 15"><path d="M8 1L2 7.5 8 14" fill="none" stroke="currentColor" stroke-width="2"/></svg>Home</span>Intensity</div>
  </div>
  <div class="row" style="top:80px"><svg class="wave" viewBox="0 0 30 26"><path d="M1 13L4 3 7 23 10 3 13 23 16 3 19 23 22 3 25 23 28 13"/></svg><span class="label">Continuous</span><span class="toggle on"></span></div>
  <div class="row" style="top:143px"><svg class="wave" viewBox="0 0 30 26"><path d="M1 13h8l3-9 4 18 3-9h10"/></svg><span class="label">Slow Pulse</span><span class="toggle"></span></div>
  <div class="row" style="top:206px"><svg class="wave" viewBox="0 0 30 26"><path d="M1 13h4l3-9 3 18 3-9h4l3-9 3 18 3-9h2"/></svg><span class="label">Medium Pulse</span><span class="toggle"></span></div>
  <div class="row" style="top:269px"><svg class="wave" viewBox="0 0 30 26"><path d="M1 13l3-9 3 18 3-11 3 9 3-12 3 14 3-9 3 8 3-10"/></svg><span class="label">Fast Pulse</span><span class="toggle"></span></div>
  <nav class="tabbar">
    <div class="tab"><svg viewBox="0 0 20 20"><path d="M3 10L10 3l7 7M5 8v9h4v-5h2v5h4V8"/></svg>Home</div>
    <div class="tab active"><svg viewBox="0 0 20 20"><path fill="currentColor" d="M6 18c-2-2-3-5-3-7l2-1 2 3V4a1 1 0 012 0v6V2.5a1 1 0 012 0V10V3.5a1 1 0 012 0V11V6a1 1 0 012 0v7c0 3-2 5-4 5z"/></svg>Intensity</div>
    <div class="tab"><svg viewBox="0 0 20 20"><circle cx="10" cy="11" r="7.5"/><path d="M10 11L7 7M10 3.5V2"/></svg>Timer</div>
    <div class="tab"><svg viewBox="0 0 20 20"><path d="M7 16V4l10-2v12"/><circle cx="5" cy="16" r="2"/><circle cx="15" cy="14" r="2"/></svg>Music</div>
    <div class="tab"><svg viewBox="0 0 20 20"><path d="M7 7H4v11h12V7h-3M10 13V2M7 5l3-3 3 3"/></svg>Share</div>
  </nav>
</section>

<!-- Timer screen -->
<section class="screen timer">
  <div class="appbar">
    <div class="status"><span>●●●●○ Carrier</span><span class="time">4:34 PM</span><span>100% <i class="battery"></i></span></div>
    <div class="navbar"><span class="back"><svg viewBox="0 0 9 15"><path d="M8 1L2 7.5 8 14" fill="none" stroke="currentColor" stroke-width="2"/></svg>Home</span>Timer</div>
  </div>
  <div class="picker">
    <span class="n" style="left:130px;top:4px;font-size:9px">22</span>
    <span class="n" style="left:130px;top:18px">23</span>
    <span class="n" style="left:130px;top:40px">24</span>
    <div class="sel"><span style="left:54px">0 <small style="font-size:13px">hours</small></span><span style="left:130px">25 <small style="font-size:13px">min</small></span></div>
    <span class="n" style="left:56px;top:92px">1</span><span class="n" style="left:130px;top:92px">26</span>
    <span class="n" style="left:56px;top:113px;font-size:11px">2</span><span class="n" style="left:130px;top:113px;font-size:11px">27</span>
    <span class="n" style="left:56px;top:131px;font-size:8px">3</span><span class="n" style="left:130px;top:131px;font-size:8px">28</span>
  </div>
  <div class="row"><span class="label">Power Saving Mode</span><span class="toggle on"></span></div>
  <div class="circle-btn start">Start</div>
  <div class="circle-btn pause">Pause</div>
  <nav class="tabbar">
    <div class="tab"><svg viewBox="0 0 20 20"><path d="M3 10L10 3l7 7M5 8v9h4v-5h2v5h4V8"/></svg>Home</div>
    <div class="tab"><svg viewBox="0 0 20 20"><path d="M6 18c-2-2-3-5-3-7l2-1 2 3V4a1 1 0 012 0v6V2.5a1 1 0 012 0V10V3.5a1 1 0 012 0V11V6a1 1 0 012 0v7c0 3-2 5-4 5z"/></svg>Intensity</div>
    <div class="tab active"><svg viewBox="0 0 20 20"><circle cx="10" cy="11" r="7.5" fill="currentColor"/><path d="M10 11L7 7M10 3.5V2" stroke="#fff"/></svg>Timer</div>
    <div class="tab"><svg viewBox="0 0 20 20"><path d="M7 16V4l10-2v12"/><circle cx="5" cy="16" r="2"/><circle cx="15" cy="14" r="2"/></svg>Music</div>
    <div class="tab"><svg viewBox="0 0 20 20"><path d="M7 7H4v11h12V7h-3M10 13V2M7 5l3-3 3 3"/></svg>Share</div>
  </nav>
</section>

<!-- Share sheet -->
<section class="screen share">
  <div class="appbar">
    <div class="status"><span>●●●●○ Carrier</span><span class="time">4:34 PM</span><span>100% <i class="battery"></i></span></div>
    <div class="navbar">Kelvo Massager</div>
  </div>
  <div class="stage">
    <div class="massager-art art" role="img" aria-label="Hand-held massager illustration, dimmed behind share sheet" style="opacity:.85"></div>
  </div>
  <div class="sheet">
    <div class="share-item"><i style="background:#5fd34a"></i>Message</div>
    <div class="share-item"><i style="background:#2a8ff0"></i>Mail</div>
    <div class="share-item"><i style="background:#4aa7e6"></i>Quillcast</div>
    <div class="share-item"><i style="background:#3b5a9a"></i>Circlebook</div>
  </div>
  <div class="cancel">Cancel</div>
</section>

<!-- Music screen -->
<section class="screen music">
  <div class="appbar">
    <div class="status"><span>●●●●○ Carrier</span><span class="time">4:34 PM</span><span>100% <i class="battery"></i></span></div>
    <div class="navbar"><span class="back"><svg viewBox="0 0 9 15"><path d="M8 1L2 7.5 8 14" fill="none" stroke="currentColor" stroke-width="2"/></svg>Home</span>Music<span class="right">Edit Playlist</span></div>
  </div>
  <div class="track" style="top:52px"><div class="cover" role="img" aria-label="Album cover: black and white portrait" style="background:linear-gradient(#555,#222)"></div><div class="meta"><div class="title">Gallant Things Happen T…</div><div class="sub">Jonah Carr <em>The Essential Jonah…</em></div></div></div>
  <div class="track" style="top:99px"><div class="cover" role="img" aria-label="Album cover: warm-toned group photo" style="background:linear-gradient(#c98a4a,#6b4a2c)"></div><div class="meta"><div class="title">Gwendolyne</div><div class="sub">Corley, Shaw and Nell <em>Greatest Hits</em></div></div></div>
  <div class="track" style="top:146px"><div class="cover" role="img" aria-label="Album cover: bright summer compilation art" style="background:linear-gradient(#e0a23a,#5a8fc4)"></div><div class="meta"><div class="title">The Gravel Man</div><div class="sub">Brine <em>Classic Soft Rock: Summer Da…</em></div></div></div>
  <div class="player">
    <svg viewBox="0 0 22 22"><path d="M3 5h2v12H3zM12 5v12L5 11zM20 5v12l-7-6z"/></svg>
    <svg viewBox="0 0 22 22"><path d="M5 4h4v14H5zM13 4h4v14h-4z"/></svg>
    <svg viewBox="0 0 22 22"><path d="M6 3l12 8-12 8z"/></svg>
    <svg viewBox="0 0 22 22"><path d="M2 5v12l7-6zM10 5v12l7-6zM17 5h2v12h-2z"/></svg>
  </div>
  <nav class="tabbar">
    <div class="tab"><svg viewBox="0 0 20 20"><path d="M3 10L10 3l7 7M5 8v9h4v-5h2v5h4V8"/></svg>Home</div>
    <div class="tab"><svg viewBox="0 0 20 20"><path d="M6 18c-2-2-3-5-3-7l2-1 2 3V4a1 1 0 012 0v6V2.5a1 1 0 012 0V10V3.5a1 1 0 012 0V11V6a1 1 0 012 0v7c0 3-2 5-4 5z"/></svg>Intensity</div>
    <div class="tab"><svg viewBox="0 0 20 20"><circle cx="10" cy="11" r="7.5"/><path d="M10 11L7 7M10 3.5V2"/></svg>Timer</div>
    <div class="tab active"><svg viewBox="0 0 20 20"><path d="M7 16V4l10-2v12"/><circle cx="5" cy="16" r="2" fill="currentColor"/><circle cx="15" cy="14" r="2" fill="currentColor"/></svg>Music</div>
    <div class="tab"><svg viewBox="0 0 20 20"><path d="M7 7H4v11h12V7h-3M10 13V2M7 5l3-3 3 3"/></svg>Share</div>
  </nav>
</section>

<!-- Albums library screen -->
<section class="screen albums">
  <div class="status"><span>●●●●○ Carrier</span><span class="time">4:34 PM</span><span>100% <i class="battery"></i></span></div>
  <div class="navbar"><span class="back">Store</span>Albums<span class="now">Now<br>Playing</span></div>
  <div class="section" style="top:55px">L</div>
  <div class="album clipped" style="top:69px;height:40px"><div class="cover" role="img" aria-label="Album cover: colourful retro print" style="background:linear-gradient(#d94a6a,#3a2a4a)"></div><div class="meta"><div class="artist">Lino Prato</div><div class="count"><b>12</b> songs, <b>41</b> min</div></div></div>
  <div class="album" style="top:114px"><div class="cover" role="img" aria-label="Album cover: figure in a warm arena scene" style="background:linear-gradient(#e2b84a,#7a3a20)"></div><div class="meta"><div class="name">The Lonely Harbor</div><div class="artist">Hal Arden &amp; The Tid…</div><div class="count"><b>1</b> song, <b>2</b> min</div></div></div>
  <div class="album" style="top:194px"><div class="cover" role="img" aria-label="Album cover: sunlit railings in teal and amber" style="background:linear-gradient(#e6b35a,#2f7f8a)"></div><div class="meta"><div class="name">Lowtide</div><div class="artist">Pale Lagoon</div><div class="count"><b>12</b> songs, <b>52</b> min</div></div></div>
  <div class="section" style="top:278px">M</div>
  <div class="album" style="top:294px"><div class="cover" role="img" aria-label="Album cover: psychedelic yellow and red artwork" style="background:linear-gradient(#f0cf3a,#d2452f)"></div><div class="meta"><div class="name">Marvel Meadow Tour</div><div class="artist">The Brightlines</div><div class="count"><b>11</b> songs, <b>37</b> min</div></div></div>
  <div class="album" style="top:382px;height:40px;align-items:flex-start"><div class="cover" role="img" aria-label="Album cover: vintage group portrait" style="height:40px;background:linear-gradient(#e8e0c8,#b9a98a)"></div><div class="meta" style="padding-top:20px"><div class="name">The Minors &amp; The…</div><div class="artist">The Minors &amp; The M…</div></div></div>
  <div class="index"><span>A</span><span>B</span><span>C</span><span>D</span><span>E</span><span>F</span><span>G</span><span>H</span><span>I</span><span>J</span><span>K</span><span>L</span><span>M</span><span>N</span><span>O</span><span>P</span><span>Q</span><span>R</span><span>S</span><span>T</span><span>U</span><span>V</span><span>W</span><span>X</span><span>Y</span><span>Z</span><span>#</span></div>
  <nav class="tabbar">
    <div class="tab"><svg viewBox="0 0 20 20"><path d="M3 5h9M3 9h9M3 13h6M14 15V4l4-1"/><circle cx="12.5" cy="15" r="1.8"/></svg>Playlists</div>
    <div class="tab"><svg viewBox="0 0 20 20"><circle cx="12" cy="7" r="3.5"/><path d="M5 18c0-4 3-6 7-6s7 2 7 6z"/></svg>Artists</div>
    <div class="tab"><svg viewBox="0 0 20 20"><path d="M9 16V3l5 2"/><circle cx="7" cy="16" r="2"/></svg>Songs</div>
    <div class="tab active"><svg viewBox="0 0 20 20"><rect x="3" y="3" width="14" height="14" rx="2" fill="currentColor"/><path d="M9 13V6l4-1v6" stroke="#fff"/></svg>Albums</div>
    <div class="tab"><svg viewBox="0 0 20 20"><circle cx="4" cy="10" r="1.3" fill="currentColor"/><circle cx="10" cy="10" r="1.3" fill="currentColor"/><circle cx="16" cy="10" r="1.3" fill="currentColor"/></svg>More</div>
  </nav>
</section>

<!-- App icon -->
<div class="appicon">
  <div class="massager-art art" role="img" aria-label="App icon artwork: orange hand-held massager with grey ribbed neck"></div>
</div>

</body>
</html>
```